Church Lanterns Over Millbrook Gospel Booklet Design

We need a booklet designed that we will be printing to hand out in our community. Wording for each page will be provided and we need graphic design to produce the layouts in a format ready for print. Booklet will be 4.75" x 4.75" square and a total of 12 pages: 1 cover page front, 1 cover page back, 10 inside pages some of which will be full spread across 2 pages.

Target Market(s)

English speaking Westerners

Industry/Entity Type

Religious

Font styles to use
Serif

Colors
ffffff
85abd2
0292cd
33b8a4
5c5c5c

Requirements
Must have
• Minimalist design with clean look described in attached document
Nice to have
• Aesthetically pleasing graphics, crisp fonts, excellent turn around times
Should not have
• Effeminate design, busy look with too much graphic and text

```html
<!DOCTYPE html>
<html lang="en">
<head>
<meta charset="utf-8">
<title>Lanterns Over Millbrook – Booklet Pages</title>
<link rel="stylesheet" href="https://fonts.googleapis.com/css2?family=Bebas+Neue&family=Questrial&family=Rubik:wght@500;700&family=Montserrat:wght@500;700;900&family=Libre+Baskerville&display=swap">
<style>
  :root {
    --white: #ffffff;
    --sky: #85abd2;
    --blue: #0292cd;
    --teal: #33b8a4;
    --teal-deep: #1aa58c;
    --ink: #5c5c5c;
    --text: #333333;
    --dark: #222222;
    --bar-blue: #4a7bb0;
    --paper-grey: #dcdcdc;
  }
  * { box-sizing: border-box; margin: 0; padding: 0; }
  html, body { width: 1200px; height: 1200px; overflow: hidden; background: var(--white); }
  body { position: relative; font-family: "Questrial", sans-serif; color: var(--text); }

  .page { position: absolute; box-shadow: 0 8px 22px rgba(0,0,0,0.18); overflow: hidden; }

  /* Cover */
  .cover { left: 414px; top: 16px; width: 372px; height: 374px; }
  .cover-photo { position: absolute; inset: 0;
    background: radial-gradient(ellipse at 50% 62%, #ffe7a6 0%, #f1b95a 18%, #b9854a 42%, #6d5a4a 70%, #3e3430 100%); }
  .cover-frame { position: absolute; left: 28px; top: 41px; width: 316px; height: 305px;
    border: 1px solid rgba(255,255,255,0.85); border-top: none; }
  .cover-frame::before, .cover-frame::after { content: ""; position: absolute; top: 0; height: 1px; background: rgba(255,255,255,0.85); width: 12px; }
  .cover-frame::before { left: 0; }
  .cover-frame::after { right: 0; }
  .cover-title { position: absolute; left: 0; right: 0; top: 24px; text-align: center;
    font-family: "Bebas Neue", sans-serif; font-size: 29px; letter-spacing: 0.5px; color: var(--white); line-height: 1; }

  /* Spreads */
  .spread { left: 227px; width: 744px; height: 372px; background: var(--white); }
  .spread-one { top: 406px; }
  .spread-two { top: 805px; }
  .leaf { position: absolute; top: 0; width: 372px; height: 372px; }
  .leaf-left { left: 0; }
  .leaf-right { left: 372px; }

  .prayer-photo { position: absolute; left: 27px; top: 27px; width: 318px; height: 115px;
    background: linear-gradient(90deg, #2d3c52 0%, #4a5a70 30%, #c9a98c 48%, #cfd6b8 70%, #e6ecd7 100%); }
  .truths-heading { position: absolute; left: 27px; top: 149px; width: 330px;
    font-family: "Rubik", sans-serif; font-weight: 500; font-size: 13px; line-height: 15px; color: var(--blue); }
  .truths { position: absolute; left: 27px; top: 190px; width: 320px; list-style: none; }
  .truths li { position: relative; padding-left: 16px; font-size: 10.5px; line-height: 13px; color: var(--text); margin-bottom: 14px; }
  .truths svg { position: absolute; left: 0; top: 2px; }

  .body-copy { font-size: 10.5px; line-height: 22px; color: var(--text); text-align: justify; }
  .rejection-copy { position: absolute; left: 27px; top: 26px; width: 318px; }

  .verse { position: absolute; left: 0; right: 0; text-align: center; color: var(--dark); }
  .quote-mark { font-family: "Montserrat", sans-serif; font-weight: 900; font-size: 38px; line-height: 1; height: 22px; color: var(--dark); }
  .wages { top: 138px; }
  .wages .lead { font-family: "Montserrat", sans-serif; font-weight: 500; font-size: 19px; margin-top: 4px; }
  .wages .big { font-family: "Montserrat", sans-serif; font-weight: 900; font-size: 33px; color: var(--blue); line-height: 36px; letter-spacing: -0.5px; }
  .wages .death-line { line-height: 46px; }
  .wages .is { font-family: "Libre Baskerville", serif; font-size: 18px; color: var(--dark); margin-right: 10px; }
  .wages .death { font-family: "Montserrat", sans-serif; font-weight: 700; font-size: 44px; color: var(--teal); letter-spacing: 1px; }
  .wages .dots { font-family: "Montserrat", sans-serif; font-weight: 900; font-size: 30px; color: var(--dark); }
  .wages .ref { font-family: "Montserrat", sans-serif; font-weight: 700; font-size: 12px; margin-top: 2px; }

  .paper-grey { background: linear-gradient(160deg, #d6d6d6, #e2e2e2 50%, #d8d8d8); }
  .hope-photo { position: absolute; inset: 0;
    background: linear-gradient(120deg, #f7dada 0%, #f8e6e2 40%, #f8f3dc 75%, #ededd6 100%); }
  .bar { position: absolute; width: 82px; height: 16px; }
  .bar-blue { background: var(--bar-blue); }
  .bar-teal { background: var(--teal-deep); }

  .section-title { position: absolute; left: 0; right: 0; top: 78px; text-align: center;
    font-family: "Montserrat", sans-serif; font-weight: 700; font-size: 11.5px; color: #15857a; letter-spacing: -0.2px; }
  .section-title::before, .section-title::after { content: ""; display: inline-block; width: 20px; height: 1px; background: var(--dark); vertical-align: middle; margin: 0 8px; }
  .alienation-copy { position: absolute; left: 46px; top: 111px; width: 286px; font-size: 12.4px; line-height: 22px; }
  .hope-copy { position: absolute; left: 26px; top: 57px; width: 320px; }

  .john { top: 192px; }
  .john .lines { font-size: 11px; line-height: 22px; color: var(--text); margin: 4px auto 0; width: 270px; }
  .john .blue { color: var(--blue); }
  .john .teal { color: var(--teal); }
  .john b { color: var(--dark); font-family: "Montserrat", sans-serif; font-weight: 700; font-size: 10.5px; }
</style>
</head>
<body>

  <section class="page cover">
    <div class="cover-photo" role="img" aria-label="Cupped hands raised toward a glowing sunset sky with a small light cross between them"></div>
    <div class="cover-frame"></div>
    <h1 class="cover-title">Lanterns Over Millbrook</h1>
  </section>

  <section class="page spread spread-one">
    <div class="leaf leaf-left">
      <div class="prayer-photo" role="img" aria-label="Woman with folded hands praying in soft natural light"></div>
      <h2 class="truths-heading">This reality establishes some foundational truths for all of us:</h2>
      <ul class="truths">
        <li><svg width="9" height="9" viewBox="0 0 10 10"><circle cx="5" cy="5" r="5" fill="#33b8a4"/><path d="M2.7 5.1 4.3 6.6 7.4 3.5" stroke="#fff" stroke-width="1.4" fill="none"/></svg>God loves us - he didn’t have to create us; we are here because he couldn’t imagine life without us.</li>
        <li><svg width="9" height="9" viewBox="0 0 10 10"><circle cx="5" cy="5" r="5" fill="#33b8a4"/><path d="M2.7 5.1 4.3 6.6 7.4 3.5" stroke="#fff" stroke-width="1.4" fill="none"/></svg>God is the proper authority in our lives - if he designed and made us, he rightfully owns us.</li>
        <li><svg width="9" height="9" viewBox="0 0 10 10"><circle cx="5" cy="5" r="5" fill="#33b8a4"/><path d="M2.7 5.1 4.3 6.6 7.4 3.5" stroke="#fff" stroke-width="1.4" fill="none"/></svg>God knows the purpose of our lives - if he designed and made us, he knows why we are here.</li>
        <li><svg width="9" height="9" viewBox="0 0 10 10"><circle cx="5" cy="5" r="5" fill="#33b8a4"/><path d="M2.7 5.1 4.3 6.6 7.4 3.5" stroke="#fff" stroke-width="1.4" fill="none"/></svg>God’s truth is the truth we need - if he designed &amp; made us, he knows what it takes for life to go well for us.</li>
      </ul>
    </div>
    <div class="leaf leaf-right">
      <p class="body-copy rejection-copy">But we, mankind, have all rejected God’s authority in our lives. And because he rightfully owns us, our rebellion against God is a grave injustice; an act of treason for which we deserve to be cut off from God forever.</p>
      <div class="verse wages">
        <div class="quote-mark">“</div>
        <div class="lead">For the</div>
        <div class="big">WAGES OF SIN</div>
        <div class="death-line"><span class="is">is</span><span class="death">DEATH</span><span class="dots">...</span></div>
        <div class="ref">(Romans 6:23)</div>
        <div class="quote-mark" style="margin-top:6px">”</div>
      </div>
    </div>
  </section>

  <section class="page spread spread-two">
    <div class="leaf leaf-left paper-grey">
      <div class="bar bar-blue" style="left:27px; top:27px;"></div>
      <h2 class="section-title">ALIENATION FROM GOD</h2>
      <p class="body-copy alienation-copy">This alienation from God is evident in a myriad of ways including poverty, crime, conflict in our relationships, and our internal struggles. But worse, when we die, we must face the conse-quences for our rejection of God by spending eternity in hell - a lake of fire created by God as the place where our treason is brought to justice.</p>
      <div class="bar bar-blue" style="left:263px; top:329px;"></div>
    </div>
    <div class="leaf leaf-right">
      <div class="hope-photo" role="img" aria-label="Faint silhouette of three crosses on a hill against a soft dawn sky"></div>
      <div class="bar bar-teal" style="left:262px; top:27px;"></div>
      <p class="body-copy hope-copy">But God does not want you to pay for your own sins. God loves us so much he sent his only son to save us. Jesus Christ died on the cross to serve our sentence for our rebellion against God and rose again on the third day. Since Christ paid our full penalty, we can be completely forgiven and reconciled to God</p>
      <div class="verse john">
        <div class="quote-mark">“</div>
        <p class="lines">For God so <span class="blue">loved the world</span> that he sent his <span class="teal">one &amp; only son</span> that whosoever <b>believes in him</b> will not perish but <b>HAVE ETERNAL LIFE.</b></p>
        <div class="quote-mark" style="margin-top:6px">”</div>
      </div>
      <div class="bar bar-teal" style="left:26px; top:329px;"></div>
    </div>
  </section>

</body>
</html>
```